Meadowbrook Setter Society - Rare dog breed club needs web design!

The Transylvanian Hound (or Erdélyi kopó) is an ancient Hungarian dog breed. These medium-sized hounds were favored by the Hungarian kings and princes for hunting bears and wolves in the Carpathian mountains of Transylvania. The breed's great adaptability to the region's extreme climates of sweltering summers and frigid winters made it an excellent all season hunting dog. This dog has a sleek appearance and stunning good looks. They are lean, appear very elegant and proud. Their erect posture and beautifully sculpted head portray great attentiveness and authority. In general, this rare breed is extremely good natured, loyal and obedient. It has a tendency to form strong attachments to its primary caretakers and will remain loyal and protective. (Please refer to existing web resources.)

The Meadowbrook Setter Society - with current website www.meadowbrooksetter-example.org - is the official breed club of Transylvanian Hound afficionados, breeders and owners in the United States, which was founded in 2010. We are looking for a web design for the new, upgraded version of this central (currenty non-functioning) website. Please do not recycle the old logo (we may choose from your suggesions and pay for it!) or any of the old texts. Please use the structure described below. Overall, the webpage serves a dual purpose: an educational one (about the breed itself) and a community-building one (inside the Club). The proposed structure of the website is as follows:

1. About the Kopó
- Breed History
- Breed Standard
- Public Education
- Photo Gallery

2. Life with a Kopó
- Health and Genetics
- Feeding and Nutrition
- Training and Activities

3. Finding a Kopó
- Is this the Right Breed for You?
- Choosing a Puppy
- FAQ
- Breeder Referral

4. The Meadowbrook Setter Society
- Constituton
- Officers and Appointees
- Code of Ethics
- Breeder Guidelines
- Membership
- Reports
- Links

5. News and Events

6. Shop

We are attaching a couple of examples of the graphics/drawings of the dogs that would be part of the design of the website. We plan to have more of these artistic depictions, nicely embedded into the background (maybe shaded out at the edges just like the drawings themselves) and less actual photos. Or a good combination of the two.

Further information upon request.

Reason: There are a few very promising design collaborations ongoing. As we moved the brief to a more artistic and graphic direction, we felt that one week of extension would be needed to get to the perfect end-product, which could include designs for sub-pages as well.

Reason: In order to make the final modifications to the leading designs, and at the request of those designers, the deadline is extended until Friday.

Target Market(s)

- MBSS Club members, dog (especially T-Hound) owners, past and future owners, breeders, puppy buyers, hunters, kennel clubs, dog show participants, vets, animal shelters, Hungarian, Romanian and other European web visitors, historians

Industry/Entity Type

Club

Font styles to use
Serif
Decorative
Script

Requirements
Must have
• - Sync with graphics of dogs (see attachments), but accentuate the rich black basic color of the dogs
- Elegance, aristocratic/noble look and feel (but not overly archaic)
- Love, companionship, dogs as family members
- Hunting usage, but no bloody associations, rather romantic ones
- Simple to use and navigate for non-web-natives
- Old world (Central European) atmosphere, even the exotic, rustic and romantic Transylvanian feel - SEE the new attachment for inspiration (this was a design plan which we discarded (mainly because of its gothic, (nazi-like), unreadable font, and the fact that the plan makes the black-looking dogs appear brown), however we loved the fact that it was not full of boxes/windows, had a marble/sand stone like continuous background, lots of little elegant graphics, the drawings embedded, etc.
Nice to have
• - Working on smartphone, iPads, etc., so dynamic website design
- Web shop to be added to functionalities in the future (?)
- English language for now, in the future can be Hungarian, Romanian, etc., so the font choice should handle various alphabets
- Focus on the dogs (likely more graphics than photos, at least on the main pages), and not on the activities/humans - the design should accentuate the black and not the tan of the graphics!
Should not have
• - Old logo from the old www.meadowbrooksetter-example.org webpage or the other logo from the Chatterbox site of the Meadowbrook Setter Society, we will have a new one (maybe designed by you!)
- Breed club, kennel club cliches
- Cutesy, adorable, cheesy design elements
- Old, stale, monolithic, archaic, snobbish, etc. look and feel
- No vampire associations

```html
<!DOCTYPE html>
<html lang="en">
<head>
<meta charset="utf-8">
<title>Meadowbrook Setter Society</title>
<link rel="stylesheet" href="https://fonts.googleapis.com/css2?family=Open+Sans:wght@400&family=Pinyon+Script&display=swap">
<style>
  :root {
    --plum-dark: #5e434a;
    --plum-mid: #7a5a64;
    --mauve-edge: #b89ba7;
    --mauve-soft: #e6d8de;
    --paper: #f7f1f3;
    --white: #ffffff;
    --ink: #2b2326;
    --rule: #a8909a;
    --dog-dark: #3a2622;
    --dog-tan: #b9845e;
  }
  * { box-sizing: border-box; margin: 0; padding: 0; }
  html, body { width: 1200px; height: 768px; overflow: hidden; }
  body {
    position: relative;
    font-family: "Open Sans", Arial, sans-serif;
    color: var(--ink);
    background: var(--paper);
  }
  .page-backdrop {
    position: absolute; inset: 0;
    background:
      radial-gradient(ellipse 55% 60% at 55% 45%, rgba(255,255,255,0.95) 0%, rgba(247,240,243,0.7) 45%, rgba(0,0,0,0) 80%),
      linear-gradient(180deg, var(--mauve-soft) 0%, #efe5e9 40%, #e4d4db 75%, var(--mauve-edge) 100%);
  }
  .page-backdrop::after {
    content: ""; position: absolute; inset: 0;
    background: radial-gradient(ellipse 90% 80% at 50% 45%, rgba(0,0,0,0) 55%, rgba(120,80,100,0.35) 100%);
  }
  .top-bar {
    position: absolute; left: 0; top: 0; width: 1200px; height: 37px;
    background: var(--plum-dark);
    border-top: 4px solid var(--plum-dark);
    box-shadow: inset 0 1px 0 rgba(255,255,255,0.55);
  }
  .main-nav {
    position: absolute; right: 89px; top: 10px;
    display: flex; gap: 34px;
  }
  .main-nav a {
    color: var(--white); text-decoration: none;
    font-size: 15px; line-height: 20px;
  }
  .club-name {
    position: absolute; left: 90px; top: 0; width: 204px; height: 56px;
    background: var(--white);
    border: 3px solid var(--plum-dark);
    border-top: none;
    display: flex; align-items: center; justify-content: center; text-align: center;
    font-size: 13px; line-height: 16px; color: var(--plum-dark);
  }
  .hero-art {
    position: absolute; left: 722px; top: 95px; width: 330px; height: 300px;
    background: radial-gradient(ellipse 48% 50% at 48% 48%, var(--dog-dark) 0%, #6b4534 40%, var(--dog-tan) 62%, rgba(185,132,94,0) 80%);
    opacity: 0.9;
  }
  .welcome-line {
    position: absolute; left: 89px;
    background: var(--white);
    font-family: "Pinyon Script", cursive;
    color: var(--ink); font-weight: 400;
    padding-left: 24px;
    white-space: nowrap;
  }
  .welcome-line--first { top: 268px; width: 291px; height: 55px; font-size: 38px; line-height: 58px; }
  .welcome-line--second {
    top: 330px; width: 556px; height: 62px; font-size: 38px; line-height: 62px;
    border-bottom: 1px solid var(--rule);
  }
  .shop-button {
    position: absolute; left: 89px; top: 398px; width: 194px; height: 44px;
    background: var(--plum-dark); color: var(--white);
    font-family: "Pinyon Script", cursive; font-size: 26px; line-height: 46px;
    text-align: center; text-decoration: none;
  }
  .section-divider { position: absolute; left: 89px; top: 440px; }
  .section-title {
    position: absolute; top: 496px;
    font-family: "Pinyon Script", cursive; font-weight: 400;
    font-size: 34px; line-height: 44px; color: var(--ink);
  }
  .news-title { left: 90px; }
  .about-title { left: 648px; }
  .date-badge { position: absolute; left: 87px; top: 557px; }
  .date-badge .day, .date-badge .month {
    position: absolute; left: 0; width: 106px; text-align: center; color: var(--white);
  }
  .date-badge .day { top: 24px; font-size: 22px; line-height: 26px; }
  .date-badge .month { top: 51px; font-size: 16px; line-height: 20px; }
  .body-copy {
    position: absolute; top: 558px;
    font-size: 13px; line-height: 18px; color: var(--ink);
  }
  .news-copy { left: 206px; width: 354px; }
  .about-copy { left: 646px; width: 466px; }
  .site-footer {
    position: absolute; left: 0; top: 713px; width: 1200px; height: 55px;
    background: var(--plum-dark);
    box-shadow: inset 0 10px 0 var(--plum-dark), inset 0 11px 0 rgba(255,255,255,0.5);
  }
  .site-footer p {
    position: absolute; left: 90px; top: 27px;
    font-family: Arial, Helvetica, sans-serif;
    font-size: 10px; line-height: 14px; color: var(--white);
  }
</style>
</head>
<body>
  <div class="page-backdrop" role="img" aria-label="Soft mauve damask-patterned marble background"></div>

  <header class="top-bar">
    <nav class="main-nav">
      <a href="#">About the Kopo</a>
      <a href="#">Life with a Kopo</a>
      <a href="#">Finding a Kopo</a>
      <a href="#">The Meadowbrook Setter Society</a>
    </nav>
  </header>
  <div class="club-name">Meadowbrook Setter Society</div>

  <div class="hero-art" role="img" aria-label="Watercolour drawing of a black and tan hound's head, shaded out at the edges"></div>

  <h1>
    <span class="welcome-line welcome-line--first">Welcome to the</span>
    <span class="welcome-line welcome-line--second">Meadowbrook Setter Society</span>
  </h1>
  <a class="shop-button" href="#">Shopiing Cart</a>

  <svg class="section-divider" width="1022" height="40" viewBox="0 0 1022 40" aria-hidden="true">
    <line x1="0" y1="17" x2="1020" y2="17" stroke="var(--rule)" stroke-width="1"/>
    <line x1="0" y1="23" x2="1020" y2="23" stroke="var(--rule)" stroke-width="1"/>
    <rect x="495" y="6" width="24" height="24" transform="rotate(45 507 18)" fill="var(--white)" stroke="var(--rule)"/>
    <rect x="499" y="10" width="16" height="16" transform="rotate(45 507 18)" fill="var(--plum-mid)"/>
  </svg>

  <h2 class="section-title news-title">News &amp; Events</h2>
  <div class="date-badge">
    <svg width="106" height="94" viewBox="0 0 106 94" aria-hidden="true">
      <rect x="0" y="2" width="106" height="8" rx="4" fill="var(--plum-dark)"/>
      <rect x="0" y="84" width="106" height="8" rx="4" fill="var(--plum-dark)"/>
      <path d="M12 8 H94 L90 20 L96 34 L90 48 L96 62 L90 76 L94 86 H12 L16 76 L10 62 L16 48 L10 34 L16 20 Z" fill="var(--plum-dark)"/>
    </svg>
    <span class="day">21</span>
    <span class="month">Mar</span>
  </div>
  <p class="body-copy news-copy">Transylvanian feel - SEE the new attachment for inspiration (this was a design plan which we discarded (mainly because of its gothic, (nazi-like), unreadable font, and the fact that the plan makes the black-looking dogs appear brown).</p>

  <h2 class="section-title about-title">Meadowbrook Setter Society</h2>
  <p class="body-copy about-copy">Transylvanian feel - SEE the new attachment for inspiration (this was a design plan which we discarded (mainly because of its gothic, (nazi-like), unreadable font, and the fact that the plan makes the black-looking dogs appear brown).</p>

  <footer class="site-footer">
    <p>Copyright © 2014 Meadowbrook Setter Society. All Rights Reserved.</p>
  </footer>
</body>
</html>
```